Vorlen - Customer Experience Software Company Web Design

*****UPDATE*****
We've been getting a lot of corporate designs through. Unfortunately this is not what we are looking for. We would like our brand to be more approachable and for the look and feel to to be a bit more fun.
Also the best designs we have received so far have followed the "less is more" approach. Im hoping any news designs will take these aspects into account.
*****************

Background:

Vorlen is a Customer Experience Technology company. We equip business and technology teams with the frameworks, tools and services to help them create compelling experiences for their customers.

Our flagship product - Vorlen CX is an open-source customer experience application framework – it enables organisation to build highly differentiated business applications to deliver compelling experiences to your customers.

Vorlen CX is designed for innovators who understand that unlocking opportunity in today’s competitive marketplace is driven by delivering a better customer experience.

Task:

We are looking for a web design (we need PSD, no HTML/CSS) for our company site through which to launch our customer experience framework product. The site will be also used as a support site, so the functional aspect of the site is as important as the visual impact for sales.

In order to help us conceptualise ideas and content we have drafted a temporary website using a standard wordpress theme (please see details below). Now we have a general idea of our requirements we like we would like to take it to the next level and get some designs with that professional edge.

Our target market are Enterprise organisations - that is senior members of the business & technology teams (Business General Managers, CTO’s, CIO’s, and Senior Architects and Senior Developers). We want something clean & fresh which is DIFFERENT from the typical corporate technology websites out there. We would like to be seen as more approachable than most large technology companies.

Words we would like to use to describe the finished design:
• Clean (we’re thinking white background with one or two key colours)
• Fresh
• Light
• Modern
• Less is more
• Web 2.0
• Fun but professional (aimed at Enterprise/Large organisations)
• Bold, clear call to action – e.g. Live Demo & Download
• Readable (but Sans Serif)

As we’re a Customer Experience company, the usability of the site is critical. The site must be functional, intuitive & easy to navigate. We want to keep the number of user clicks to the bare minimum possible.

Other aspects, which we would like to incorporate into the site
• Home Page banner slider
• Client logon
• Newsletter sign up
• Social media links – Facebook, LinkedIn (for starters)
• Rich footer links

Some websites we like
• http://brightpanelworks.example - clean, light, modern & intuitive
• http://www.tamsoledrik.example - bold, clear messaging
• http://www.opengridhub.example/markup/emblem - punchy, colourful
• http://postwren.example/ - modern, clear messaging, colourful, rich footer area

Target Market(s)

Enterprise organisations - that is senior members of the business & technology teams (Business General Managers, CTO’s, CIO’s, Senior Devs)

Industry/Entity Type

Business

Requirements
Must have
• - Design Specs: Accepted file formats: During the design phase adobe PSD or JPEG are OK (if you need to upload files), but for the handover we'll need PSD only with all the original layers.
- The width needs to be a size that will work with every size computer screen
- Need to use cross-platform compatible font
- The graphic elements used for the design must be copyright free

Current test site
- URL http://vorlen.example/wp-admin
- username: artmarket
- password: artmarket

IMPORTANT NOTE REGARDING OUR CURRENT TEST SITE:

This is a very basic version of a site to help us generate requirements. This design is only a starting point/input and is not locked in stone i.e. we do not simply want this site simply tweaked around the edges.

We are looking for you to use all of your graphic design skills and experience to create a truly awesome site design!

```html
<!DOCTYPE html>
<html lang="en">
<head>
<meta charset="utf-8">
<title>Vorlen – The Customer Experience Framework</title>
<link href="https://fonts.googleapis.com/css2?family=PT+Sans+Narrow:wght@400;700&family=Ropa+Sans&family=Arimo:wght@400;700&display=swap" rel="stylesheet">
<style>
:root{
  --blue:#1b9de6;
  --blue-dark:#1d86c8;
  --ink:#3c3c3c;
  --text:#5a5a5a;
  --muted:#8a8a8a;
  --page:#f7f7f7;
  --panel:#ffffff;
  --night:#1c1c1c;
  --night-2:#2b2b2b;
  --grey-btn:#7b7b7b;
  --line:#e2e2e2;
}
*{box-sizing:border-box;margin:0;padding:0}
html,body{width:1200px;height:1180px;overflow:hidden}
body{background:var(--page);font-family:"Arimo",Arial,sans-serif;color:var(--text);position:relative}
.abs{position:absolute}
.backdrop{position:absolute;left:0;top:0;width:1200px;height:1180px}
.backdrop.front{z-index:2;pointer-events:none}

/* every drawn element sits above the panel and the dark wave */
header .abs,.slider .abs,.content .abs,.social-row .abs,.foot .abs{z-index:3}

/* header */
.brand{left:170px;top:44px}
.brand-name{font-family:"Ropa Sans",sans-serif;font-size:34px;letter-spacing:2px;color:var(--blue);line-height:1;display:flex;align-items:center;gap:8px}
.brand-name .dot{width:12px;height:12px;background:var(--blue);display:inline-block}
.brand-tag{font-family:"Ropa Sans",sans-serif;font-size:13px;color:#555;margin-top:2px}
.home-tab{left:503px;top:0;width:65px;height:137px;background:var(--blue);border-radius:0 0 14px 14px}
.nav{top:97px;left:0}
.nav a{position:absolute;font-family:"Ropa Sans",sans-serif;font-size:18px;color:#444;text-decoration:none;letter-spacing:.5px;white-space:nowrap}
.nav a.current{color:#fff}
header .nav{z-index:4}

/* slider */
.arrow{width:38px;height:38px;border-radius:50%;border:1px solid #cfcfcf;background:#fafafa;box-shadow:0 1px 2px rgba(0,0,0,.15);display:flex;align-items:center;justify-content:center}
.slide-title{left:235px;top:220px;font-family:"PT Sans Narrow",sans-serif;font-weight:700;font-size:29px;color:var(--ink)}
.slide-sub{left:245px;top:258px;font-family:"PT Sans Narrow",sans-serif;font-size:23px;color:var(--ink)}
.slide-art{left:522px;top:168px;width:424px;height:254px;border-radius:18px;background:radial-gradient(ellipse at 60% 40%,#5cc4f2 0%,#bcd9e6 55%,#f1f3f4 100%)}

/* content panel */
.panel{left:143px;top:440px;width:892px;height:452px;background:var(--panel);border-radius:8px;box-shadow:0 0 3px rgba(0,0,0,.05);z-index:1}
.lead{left:162px;top:460px;font-family:"PT Sans Narrow",sans-serif;font-weight:400;font-size:22px;color:var(--blue);padding-bottom:3px;border-bottom:1px solid var(--line);width:410px;white-space:nowrap}
.copy{left:162px;width:545px;font-size:9.6px;line-height:14.3px;color:var(--text)}
.subhead{left:161px;font-size:13px;font-weight:400;color:#555}
.readmore{left:602px;top:760px;width:96px;height:20px;background:linear-gradient(#4cb8f2,#1b9de6);border-radius:2px;color:#fff;font-size:10.5px;display:flex;align-items:center;justify-content:center;gap:6px}
.divider{left:732px;top:526px;width:1px;height:312px;background:linear-gradient(transparent,#e3e3e3 20%,#e3e3e3 80%,transparent)}

/* sidebar */
.demo-bubble{left:762px;top:478px;width:96px;height:62px;background:linear-gradient(#2ba6ea,#1b86cc);border-radius:12px;color:#fff;font-weight:700;font-size:17px;display:flex;align-items:center;justify-content:center}
.demo-art{left:852px;top:468px;width:134px;height:107px;border-radius:8px;background:linear-gradient(160deg,#3a3f9a,#8a8fa8 60%,#d8d8dc)}
.login{left:756px;top:590px;width:257px;height:181px;border:1px solid #d6d6d6;border-radius:5px;background:#f1f1f1;overflow:hidden}
.login-head{height:29px;background:linear-gradient(#6b6b6b,#3f3f3f);color:#fff;font-family:"PT Sans Narrow",sans-serif;font-size:19px;padding-left:18px;line-height:29px}
.field-label{font-size:11px;color:#444;white-space:nowrap}
.field{width:167px;height:18px;background:#fff;border:1px solid #dcdcdc}
.check{width:11px;height:11px;border:1px solid #6f8aa8;background:#fff}
.btn-dark{left:840px;top:722px;width:71px;height:18px;border-radius:9px;background:linear-gradient(#666,#333);color:#fff;font-style:italic;font-size:12.5px;display:flex;align-items:center;justify-content:center}
.forgot{left:904px;top:748px;font-size:10.5px;color:#333;white-space:nowrap}
.newsletter{left:756px;top:785px;width:268px;height:95px;background:#f1f1f1;border:1px solid #d9d9d9;border-radius:3px}
.newsletter-title{left:806px;top:797px;font-family:"PT Sans Narrow",sans-serif;font-size:22px;color:#555;width:170px;text-align:center;white-space:nowrap}
.btn-grey{border-radius:13px;background:linear-gradient(#8a8a8a,#6a6a6a);color:#fff;display:flex;align-items:center;justify-content:center}
.signup{left:827px;top:833px;width:103px;height:25px;font-family:"PT Sans Narrow",sans-serif;font-size:15px}

/* social */
.follow{left:740px;top:918px;font-family:"Ropa Sans",sans-serif;font-size:18px;color:#555}
.social{width:29px;height:29px;border-radius:5px}
.social.one{left:833px;top:918px;background:#4ec2ee}
.social.two{left:871px;top:918px;background:#3c5a9a}
.social.three{left:909px;top:918px;background:#1d87b9}

/* footer */
.foot-head{font-size:13px;font-weight:700;color:#fff;top:1006px;white-space:nowrap}
.foot-links{top:1039px;list-style:none}
.foot-links li{font-size:11.5px;color:#9a9a9a;line-height:21.4px;white-space:nowrap}
.email{left:822px;top:1035px;width:179px;height:25px;background:#fff;border-radius:5px;font-size:11.5px;color:#222;padding-left:18px;line-height:25px}
.subscribe{left:856px;top:1072px;width:125px;height:23px;font-size:12px;background:linear-gradient(#8b8b8b,#6d6d6d)}
.copyright{left:0;width:1236px;top:1159px;text-align:center;font-size:9.5px;color:#8c8c8c}
</style>
</head>
<body>

<svg class="backdrop" viewBox="0 0 1200 1180" aria-hidden="true">
  <path d="M0,0 L1200,0 L1200,107 C1000,50 700,10 0,0 Z" fill="#1b9de6"/>
</svg>

<div class="abs panel"></div>

<svg class="backdrop front" viewBox="0 0 1200 1180" aria-hidden="true">
  <defs>
    <linearGradient id="night" x1="0" y1="0" x2="1" y2="1">
      <stop offset="0" stop-color="#141414"/>
      <stop offset="1" stop-color="#2e2e2e"/>
    </linearGradient>
  </defs>
  <path d="M0,758 C250,860 500,880 760,935 C950,975 1080,995 1200,1008 L1200,1180 L0,1180 Z" fill="url(#night)"/>
</svg>

<header>
  <div class="abs brand">
    <div class="brand-name"><span class="dot"></span>VORLEN</div>
    <div class="brand-tag">The Customer Experience Framework</div>
  </div>
  <div class="abs home-tab"></div>
  <nav class="abs nav">
    <a class="current" style="left:515px">HOME</a>
    <a style="left:588px">ABOUT</a>
    <a style="left:672px">PRODUCTS</a>
    <a style="left:788px">SUPPORT</a>
    <a style="left:891px">BLOG</a>
  </nav>
</header>

<section class="slider">
  <div class="abs arrow" style="left:145px;top:280px"><svg width="12" height="14" viewBox="0 0 12 14"><path d="M9,1 L3,7 L9,13" fill="none" stroke="#333" stroke-width="3"/></svg></div>
  <div class="abs arrow" style="left:997px;top:280px"><svg width="12" height="14" viewBox="0 0 12 14"><path d="M3,1 L9,7 L3,13" fill="none" stroke="#333" stroke-width="3"/></svg></div>
  <div class="abs slide-title">Customer Experience</div>
  <div class="abs slide-sub">Application Frame Work</div>
  <div class="abs slide-art" role="img" aria-label="Illustration of blue figures seated in chairs watching a presenter point at a bar chart board"></div>
</section>

<main class="content">
  <h1 class="abs lead">Create Compelling Experiences For Your Customers</h1>
  <p class="abs copy" style="top:498px">Vorlen is a customer experience application framework – it enables you to build highly differentiated business applications<br>to deliver compelling experiences to your customers.</p>
  <p class="abs copy" style="top:541px">Vorlen is designed for innovators who understand that unlocking opportunity in today's competitive marketplace is driven by<br>delivering a better customer experience.</p>
  <h2 class="abs subhead" style="top:581px">Opportunity though customer experience innovation</h2>
  <p class="abs copy" style="top:608px">Turn the experience you deliver to your customers into competitive advantage. Vorlen's customer experience framework is the flexible and practical way for enterprise organisations to create and manage compelling experiences. It gives you full control over how you wish to interact with your customers, and allows you to tailor experiences that grow your brand.</p>
  <h2 class="abs subhead" style="top:667px">True differentiation</h2>
  <p class="abs copy" style="top:694px">There is no one-size-fits-all application, because every business is unique! We believe in technology as a business differentiator, and flexible, cutting edge technology the key to success. If you're serious about differentiation, and want to create powerful experiences to connect with your customers in exciting new ways, we can help create experiences that your competitors can't match.</p>
  <div class="abs readmore"><svg width="9" height="9" viewBox="0 0 9 9"><path d="M1,1 L4,4.5 L1,8 M5,1 L8,4.5 L5,8" fill="none" stroke="#fff" stroke-width="1.3"/></svg>Readmore</div>
  <div class="abs divider"></div>

  <aside>
    <div class="abs demo-art" role="img" aria-label="Desktop computer with keyboard and mouse showing the demo application"></div>
    <div class="abs demo-bubble">Live Demo</div>

    <div class="abs login">
      <div class="login-head">Client Login</div>
    </div>
    <div class="abs field-label" style="left:766px;top:635px">User Name :</div>
    <div class="abs field" style="left:836px;top:633px"></div>
    <div class="abs field-label" style="left:768px;top:664px">Password&nbsp;&nbsp;:</div>
    <div class="abs field" style="left:836px;top:662px"></div>
    <div class="abs check" style="left:843px;top:692px"></div>
    <div class="abs field-label" style="left:860px;top:691px">Reminder me</div>
    <div class="abs btn-dark">Login</div>
    <div class="abs forgot">forgot password ?</div>

    <div class="abs newsletter"></div>
    <div class="abs newsletter-title">News Letter Signup</div>
    <div class="abs btn-grey signup">Signup Free</div>
  </aside>
</main>

<div class="social-row">
  <div class="abs follow">Follow Us</div>
  <div class="abs social one" role="img" aria-label="Social network link"></div>
  <div class="abs social two" role="img" aria-label="Social network link"></div>
  <div class="abs social three" role="img" aria-label="Professional network link"></div>
</div>

<footer class="foot">
  <div class="abs foot-head" style="left:220px">VORLEN</div>
  <ul class="abs foot-links" style="left:221px"><li>Home</li><li>Products</li><li>Support</li><li>Blog</li><li>About</li></ul>
  <div class="abs foot-head" style="left:400px">Getting Started</div>
  <ul class="abs foot-links" style="left:401px"><li>Demo</li><li>Documentation</li><li>Download</li></ul>
  <div class="abs foot-head" style="left:621px">Support</div>
  <ul class="abs foot-links" style="left:622px"><li>Contact Us</li><li>Vorlen Services</li><li>Vorlen Support</li></ul>
  <div class="abs foot-head" style="left:822px">Subscribe to Our News Letter</div>
  <div class="abs email">Email Address</div>
  <div class="abs btn-grey subscribe">Subscribe</div>
  <div class="abs copyright">Copyright © 2011 vorlen.example All Rights Reserved.</div>
</footer>

</body>
</html>
```